Tidal Ledger

Please see attached Word document for requirements. I want the website to be one page.

Coding

Coded - Design and coding required

Number of Pages Required

1 page

Colors
0054AA
0677BA
7BADD7
CADEEF
E8F1F8

```html
<!DOCTYPE html>
<html lang="en">
<head>
<meta charset="utf-8">
<title>Tidal Ledger — Smarter Rosters</title>
<link href="https://fonts.googleapis.com/css2?family=Inter:wght@400;500;600;700;800&display=swap" rel="stylesheet">
<style>
:root{
  --blue-900:#0054AA;
  --blue-700:#0677BA;
  --blue-400:#7BADD7;
  --blue-200:#CADEEF;
  --blue-100:#E8F1F8;
  --navy:#0B2340;
  --navy-deep:#071A33;
  --ink:#0E1A2B;
  --muted:#5B6B80;
  --line:#E3EAF2;
  --white:#fff;
}
*{box-sizing:border-box;margin:0;padding:0}
html,body{width:1200px;height:4677px;overflow:hidden}
body{font-family:"Inter",sans-serif;color:var(--ink);background:#fff;position:relative}
.abs{position:absolute}
.eyebrow{font-size:10px;font-weight:700;letter-spacing:.14em;color:var(--blue-700);text-transform:uppercase;display:flex;align-items:center;gap:8px}
.eyebrow::before{content:"";width:16px;height:1px;background:var(--blue-400)}
.eyebrow.center{justify-content:center}
.h2{font-size:34px;font-weight:800;letter-spacing:-.03em;line-height:1.1}
.lead{font-size:14px;line-height:1.75;color:var(--muted)}
.btn{display:inline-flex;align-items:center;justify-content:center;border-radius:6px;font-size:12px;font-weight:600;height:40px;padding:0 24px}
.btn-primary{background:var(--blue-900);color:#fff}
.btn-ghost{background:#fff;border:1px solid var(--line);color:var(--ink)}

/* nav */
.nav{top:0;left:0;width:1200px;height:42px}
.brand{display:flex;align-items:center;gap:9px;font-size:14px;font-weight:700;color:var(--ink)}
.brand-dot{width:28px;height:28px;border-radius:7px;background:var(--blue-900)}
.nav-links{left:362px;top:2px;height:36px;width:388px;border:1px solid var(--line);border-radius:18px;display:flex;justify-content:space-around;align-items:center;font-size:11px;color:var(--muted);background:#fff}
.nav .btn{height:36px;font-size:11px;padding:0 18px}

/* hero */
.hero{top:42px;left:0;width:1200px;height:545px;background:linear-gradient(180deg,#fff 0%,#F6FAFD 100%)}
.badge{left:149px;top:72px;height:31px;padding:0 14px 0 8px;border:1px solid var(--blue-200);border-radius:16px;background:var(--blue-100);font-size:9.5px;font-weight:700;color:var(--blue-900);letter-spacing:.08em;display:flex;align-items:center;gap:10px}
.badge i{width:18px;height:18px;border-radius:50%;background:var(--blue-900)}
.hero h1{left:147px;top:124px;font-size:54px;font-weight:800;letter-spacing:-.05em;line-height:59px}
.hero h1 .accent{color:var(--blue-900);text-decoration:underline;text-decoration-thickness:3px;text-underline-offset:4px}
.hero .lead{left:149px;top:324px;width:400px;font-size:13.5px}
.hero-ctas{left:149px;top:432px;display:flex;gap:12px}
.proof{left:149px;top:517px;display:flex;align-items:center;gap:8px;font-size:10px;color:var(--muted)}
.avatars{display:flex}
.avatars span{width:24px;height:24px;border-radius:50%;border:2px solid #fff;margin-left:-6px;background:var(--blue-700);color:#fff;font-size:7px;font-weight:700;display:flex;align-items:center;justify-content:center}
.avatars span:first-child{margin-left:0;background:var(--blue-900)}
.avatars span:nth-child(3){background:var(--blue-400)}
.stars{color:#E7A400;font-size:8px;letter-spacing:1px}
.proof b{color:var(--ink)}
.photo-frame{left:622px;top:136px;width:451px;height:343px;border-radius:18px;background:var(--blue-200);padding:10px;box-shadow:0 20px 50px rgba(0,84,170,.15)}
.photo{width:100%;height:100%;border-radius:12px;background:linear-gradient(135deg,#8FA9B8 0%,#C9D4DA 45%,#6E8597 100%)}
.float{background:#fff;border-radius:10px;box-shadow:0 10px 30px rgba(11,35,64,.14);padding:9px 14px}
.float-cost{left:614px;top:120px;width:158px}
.float-cost small{font-size:7px;font-weight:700;letter-spacing:.1em;color:var(--blue-700)}
.float-cost div{font-size:20px;font-weight:800;display:flex;align-items:center;gap:6px;margin-top:2px}
.float-cost em{font-style:normal;font-size:8px;background:#DDF5E6;color:#1E8C4E;border-radius:8px;padding:1px 5px}
.float-ai{left:955px;top:301px;font-size:9px;font-weight:600;display:flex;align-items:center;gap:6px;padding:8px 12px}
.float-ai i{width:7px;height:7px;border-radius:50%;background:#22B35E}
.float-pub{left:862px;top:430px;width:218px;display:flex;align-items:center;gap:10px}
.float-pub .tick{width:28px;height:28px;border-radius:7px;background:var(--blue-900);display:flex;align-items:center;justify-content:center;flex:none}
.float-pub b{display:block;font-size:10px}
.float-pub span{font-size:8px;color:var(--muted)}

/* trusted band */
.trusted{top:587px;left:0;width:1200px;height:118px;border-top:1px solid var(--line);border-bottom:1px solid var(--line);background:#FAFCFE;overflow:hidden}
.trusted p{position:absolute;top:30px;width:100%;text-align:center;font-size:10px;font-weight:700;letter-spacing:.16em;color:var(--muted)}
.logo-row{position:absolute;top:62px;left:31px;display:flex;gap:50px;font-size:13px;font-weight:600;color:#B4C6D8;white-space:nowrap}
.logo-row i{font-style:normal;color:#C7D4E0}

/* why */
.why-head{left:103px;top:740px}
.why-head .h2{margin-top:10px}
.why-head .lead{margin-top:14px;width:470px}
.card{border:1px solid var(--line);border-radius:14px;background:#fff;padding:24px 22px}
.card .ico{width:40px;height:40px;border-radius:9px;background:var(--blue-100);margin-bottom:26px;display:flex;align-items:center;justify-content:center}
.card h3{font-size:13px;font-weight:700;margin-bottom:9px}
.card p{font-size:11.5px;line-height:1.65;color:var(--muted)}
.stat{font-size:30px;font-weight:800;color:var(--blue-900);letter-spacing:-.03em}
.stat-sub{font-size:10.5px;color:var(--muted);margin-top:2px}

/* industries */
.ind-head{left:103px;top:1540px;width:470px}
.ind-head .h2{margin-top:12px}
.ind-head .lead{margin-top:14px}
.tags{display:flex;flex-wrap:wrap;gap:10px 10px;margin-top:22px;width:480px}
.tag{border:1px solid var(--line);border-radius:16px;padding:7px 14px;font-size:11.5px;font-weight:600;color:#33445A;background:#fff}
.ind-grid{left:650px;top:1548px;width:482px;display:grid;grid-template-columns:repeat(3,1fr);gap:10px}
.ind{height:86px;border:1px solid var(--line);border-radius:10px;background:#fff;display:flex;flex-direction:column;align-items:center;justify-content:center;gap:10px;font-size:10.5px;font-weight:600;color:#33445A;box-shadow:0 4px 14px rgba(11,35,64,.04)}
.ind i{width:22px;height:22px;border-radius:5px;background:var(--blue-200)}
.ind.more{background:var(--blue-100);border-color:var(--blue-400);color:var(--blue-900)}
.ind.more i{background:none;font-style:normal;font-size:22px;height:auto;width:auto;line-height:1}

/* testimonials */
.stories{top:1916px;left:0;width:1200px;height:574px;background:linear-gradient(180deg,var(--navy-deep),var(--navy))}
.stories .eyebrow{position:absolute;top:100px;width:100%;color:var(--blue-400)}
.stories h2{position:absolute;top:120px;width:100%;text-align:center;color:#fff}
.stories .sub{position:absolute;top:178px;width:100%;text-align:center;font-size:14px;color:#9FB3CC}
.quote{position:absolute;top:253px;width:332px;height:232px;border:1px solid rgba(123,173,215,.22);border-radius:14px;background:rgba(255,255,255,.04);padding:28px 24px}
.quote .stars{font-size:10px}
.quote p{margin-top:16px;color:#D6E2EF;font-style:italic;font-size:12.5px;line-height:1.85}
.who{position:absolute;left:24px;bottom:28px;display:flex;align-items:center;gap:12px}
.who span{width:34px;height:34px;border-radius:50%;background:var(--blue-700);color:#fff;font-size:10px;font-weight:700;display:flex;align-items:center;justify-content:center}
.who b{display:block;color:#fff;font-size:11.5px}
.who small{color:#7E93AE;font-size:9.5px}

/* pricing */
.pricing-head{top:2532px;left:0;width:1200px;text-align:center}
.pricing-head .h2{margin-top:14px}
.pricing-head .lead{margin:16px auto 0;width:470px}
.plan{position:absolute;top:2713px;width:330px;height:430px;border:1px solid var(--line);border-radius:16px;background:#fff;padding:30px 26px}
.plan.pop{top:2711px;height:444px;border:2px solid var(--blue-400);box-shadow:0 20px 50px rgba(0,84,170,.13)}
.pop-badge{position:absolute;top:-10px;left:50%;transform:translateX(-50%);background:var(--blue-900);color:#fff;font-size:9px;font-weight:700;border-radius:10px;padding:4px 16px}
.plan .tier{font-size:10px;font-weight:700;letter-spacing:.14em;color:var(--blue-700)}
.price{margin-top:10px;display:flex;align-items:baseline;gap:2px}
.price sup{font-size:15px;font-weight:700;align-self:center}
.price b{font-size:44px;font-weight:800;letter-spacing:-.04em}
.price small{font-size:11px;color:var(--blue-400)}
.plan .desc{font-size:11.5px;color:var(--muted);line-height:1.55;margin-top:4px;padding-bottom:22px;border-bottom:1px solid var(--line)}
.plan ul{list-style:none;margin-top:20px}
.plan li{display:flex;align-items:center;gap:10px;font-size:11.5px;color:#33445A;height:25.5px}
.plan li::before{content:"";width:13px;height:13px;border-radius:50%;background:var(--blue-200);flex:none;box-shadow:inset 0 0 0 3.5px var(--blue-100)}
.plan .btn{position:absolute;left:26px;right:26px;bottom:26px;height:38px;justify-content:flex-start;padding-left:12px}
.custom{font-size:28px;font-weight:800;letter-spacing:-.03em;color:var(--blue-900);margin-top:8px}

/* cta */
.cta{top:3250px;left:0;width:1200px;height:445px;background:linear-gradient(180deg,var(--blue-100),#F3F8FC);overflow:hidden}
.cta::before,.cta::after{content:"";position:absolute;border:1px solid var(--blue-200);border-radius:50%}
.cta::before{width:420px;height:420px;left:-60px;top:40px}
.cta::after{width:420px;height:420px;right:-80px;top:130px}
.cta-inner{position:absolute;top:100px;width:100%;text-align:center}
.cta h2{font-size:40px;font-weight:800;letter-spacing:-.03em;line-height:1.12;color:#3A5470;margin-top:16px}
.cta .lead{width:470px;margin:20px auto 0}
.cta-btns{display:flex;justify-content:center;gap:12px;margin-top:30px}

/* contact */
.contact-head{left:103px;top:3795px;width:480px}
.contact-head .h2{margin-top:12px}
.contact-head .lead{margin-top:18px;font-size:13px;line-height:1.4}
.info{margin-top:8px}
.info-row{display:flex;align-items:center;gap:12px;height:58px}
.info-row i{width:40px;height:40px;border-radius:9px;background:var(--blue-100);display:flex;align-items:center;justify-content:center}
.info-row b{display:block;font-size:11px}
.info-row small{font-size:11px;color:var(--blue-700)}
.form{left:652px;top:3793px;width:479px;height:485px;border-radius:16px;background:#fff;border-top:3px solid var(--blue-700);box-shadow:0 20px 50px rgba(11,35,64,.1);padding:30px 34px}
.field{margin-bottom:16px}
.field label{display:block;font-size:9.5px;font-weight:700;letter-spacing:.12em;color:#33445A;margin-bottom:7px}
.input{height:36px;border:1px solid var(--line);border-radius:7px;background:#F7FAFC;font-size:11px;color:#9AA8B8;display:flex;align-items:center;padding:0 13px}
.row2{display:flex;gap:16px}.row2 .field{flex:1}
.select{justify-content:space-between;color:#33445A;background:#fff}
.textarea{height:82px;align-items:flex-start;padding-top:12px}
.form .btn{width:100%;height:40px;margin-top:8px}

/* footer */
.footer{top:4375px;left:0;width:1200px;height:302px;background:var(--navy-deep)}
.footer .brand{position:absolute;left:103px;top:60px;color:#fff}
.footer .about{position:absolute;left:103px;top:108px;width:240px;font-size:11px;line-height:1.7;color:#7E93AE}
.fcol{position:absolute;top:52px}
.fcol h4{font-size:9.5px;letter-spacing:.16em;color:#6E84A0;font-weight:700;margin-bottom:14px}
.fcol a{display:block;font-size:11.5px;color:#9FB3CC;text-decoration:none;height:25px}
.fbottom{position:absolute;left:103px;right:69px;top:250px;border-top:1px solid rgba(123,173,215,.15);padding-top:14px;display:flex;justify-content:space-between;font-size:10px;color:#5E7592}
</style>
</head>
<body>

<header class="nav abs">
  <div class="brand abs" style="left:55px;top:6px"><span class="brand-dot"></span>Tidal Ledger</div>
  <nav class="nav-links abs"><span>Features</span><span>Industries</span><span>Pricing</span><span>Reviews</span><span>Contact</span></nav>
  <span class="btn btn-ghost abs" style="left:926px;top:2px">Book Demo</span>
  <span class="btn btn-primary abs" style="left:1035px;top:2px">Get Started →</span>
</header>

<section class="hero abs">
  <div class="badge abs"><i></i>AI-POWERED WORKFORCE PLATFORM</div>
  <h1 class="abs">Smarter Rosters.<br><span class="accent">Zero Friction.</span><br>Any Industry.</h1>
  <p class="lead abs">Tidal Ledger automates scheduling, ensures compliance, and cuts admin time by 80% — so your team can focus on people, not paperwork.</p>
  <div class="hero-ctas abs"><span class="btn btn-primary">Start Free Trial →</span><span class="btn btn-ghost">Book a Demo</span></div>
  <div class="proof abs">
    <div class="avatars"><span>NT</span><span>OR</span><span>MK</span><span>+</span></div>
    <div><div class="stars">★★★★★</div><b>500+ companies</b> already scheduling smarter</div>
  </div>
  <div class="photo-frame abs"><div class="photo" role="img" aria-label="Two colleagues celebrating with a high five at an office desk"></div></div>
  <div class="float float-cost abs"><small>LABOUR COST THIS WEEK</small><div>$28,400 <em>↓18%</em></div></div>
  <div class="float float-ai abs"><i></i>AI scheduling active</div>
  <div class="float float-pub abs"><span class="tick"><svg width="12" height="12" viewBox="0 0 12 12"><path d="M2 6.5l2.5 2.5L10 3" stroke="#fff" stroke-width="2" fill="none"/></svg></span><div><b>Roster Published</b><span>Compliance verified · All shifts filled</span></div></div>
</section>

<section class="trusted abs">
  <p>TRUSTED BY LEADING OPERATIONS TEAMS WORLDWIDE</p>
  <div class="logo-row"><span>Quayside Stays</span><i>◆</i><span>FreightWell Asia</span><i>◆</i><span>GuardLine Co</span><i>◆</i><span>StageHall Group</span><i>◆</i><span>Forgeworks Ltd</span><i>◆</i><span>Metro Aisle Co</span></div>
</section>

<section class="why-head abs">
  <div class="eyebrow">WHY TIDAL LEDGER</div>
  <h2 class="h2">Built different,<br>by design</h2>
  <p class="lead">Every decision engineered for the operations leader who needs speed, precision, and peace of mind.</p>
</section>
<div class="card abs" style="left:103px;top:962px;width:247px;height:209px"><div class="ico"><svg width="14" height="14" viewBox="0 0 14 14"><path d="M8 1L3 8h4l-1 5 5-7H7z" fill="#0677BA"/></svg></div><h3>Instant Automation</h3><p>Generate fair, compliant rosters in seconds. Hours of admin reduced to a single click.</p></div>
<div class="card abs" style="left:363px;top:962px;width:247px;height:209px;opacity:.85"><div class="stat">80%</div><div class="stat-sub">reduction in scheduling admin time</div></div>
<div class="card abs" style="left:622px;top:966px;width:249px;height:209px;opacity:.8"><div class="ico"></div><h3>Learns Your Team</h3><p>Our AI studies patterns, preferences, and constraints — getting smarter with every roster cycle.</p></div>
<div class="card abs" style="left:884px;top:970px;width:247px;height:209px;opacity:.45"><div class="stat">22%</div><div class="stat-sub">average labour cost reduction in Q1</div></div>
<div class="card abs" style="left:103px;top:1194px;width:507px;height:209px;opacity:.3"><div class="ico"></div><h3>Real Cost Savings — Not Promises</h3><p>Eliminate overtime leakage, reduce agency spend, and optimise staffing levels across every site and shift. Our customers see measurable ROI within the first pay cycle.</p></div>
<div class="card abs" style="left:622px;top:1198px;width:249px;height:209px;opacity:.12;border-color:transparent"><div class="ico"></div><h3>Always Compliant</h3><p>Award rules, break laws and fatigue limits checked automatically on every shift you publish.</p></div>

<section class="ind-head abs">
  <div class="eyebrow">INDUSTRIES SERVED</div>
  <h2 class="h2">Every workforce,<br>everywhere</h2>
  <p class="lead">Healthcare or hospitality, logistics or live events — Tidal Ledger handles the complexity of your world, not a generic version of it.</p>
  <div class="tags"><span class="tag">Healthcare</span><span class="tag">Retail</span><span class="tag">Hospitality</span><span class="tag">Logistics</span><span class="tag">Manufacturing</span><span class="tag">Security</span><span class="tag">Events</span><span class="tag">Transport</span></div>
</section>
<div class="ind-grid abs">
  <div class="ind"><i></i>Healthcare</div><div class="ind"><i></i>Retail</div><div class="ind"><i></i>Hospitality</div>
  <div class="ind"><i></i>Logistics</div><div class="ind"><i></i>Manufacturing</div><div class="ind"><i></i>Security</div>
  <div class="ind"><i></i>Events</div><div class="ind"><i></i>Transport</div><div class="ind more"><i>+</i>More</div>
</div>

<section class="stories abs">
  <div class="eyebrow center">CUSTOMER STORIES</div>
  <h2 class="h2">Trusted by operations leaders</h2>
  <p class="sub">The numbers speak — but the people behind them speak louder.</p>
  <div class="quote" style="left:103px"><div class="stars">★★★★★</div><p>"Tidal Ledger cut our scheduling from 4 hours a week to under 20 minutes. The compliance engine alone has saved us from two potential award-breach situations."</p><div class="who"><span>NT</span><div><b>Nora T.</b><small>Operations Manager, Bayview Care</small></div></div></div>
  <div class="quote" style="left:452px"><div class="stars">★★★★★</div><p>"We run 23 retail locations and the multi-site view is a game changer. Overtime costs dropped 22% in Q1 — the ROI was immediate and undeniable."</p><div class="who"><span>OR</span><div><b>Owen R.</b><small>Head of People, Shelfline Stores</small></div></div></div>
  <div class="quote" style="left:800px"><div class="stars">★★★★★</div><p>"Staff love the self-service app. Shift swaps used to be a group-chat nightmare. Now everything lives in Tidal Ledger and managers approve in one tap."</p><div class="who"><span>MK</span><div><b>Maya K.</b><small>General Manager, Pier Lane Hotels</small></div></div></div>
</section>

<section class="pricing-head abs">
  <div class="eyebrow center">SIMPLE PRICING</div>
  <h2 class="h2">Transparent. Flexible. Fair.</h2>
  <p class="lead">Start free — no credit card required. Scale exactly when you need to.</p>
</section>
<div class="plan" style="left:103px">
  <div class="tier">STARTER</div>
  <div class="price"><sup>$</sup><b>29</b><small>/month</small></div>
  <p class="desc">Perfect for small teams getting started with smarter scheduling.</p>
  <ul><li>Up to 25 staff members</li><li>1 location</li><li>AI roster generation</li><li>Mobile app (iOS &amp; Android)</li><li>Basic compliance checks</li><li>Email support</li></ul>
  <span class="btn btn-ghost">Start Free Trial</span>
</div>
<div class="plan pop" style="left:452px">
  <span class="pop-badge">Most Popular</span>
  <div class="tier">PROFESSIONAL</div>
  <div class="price"><sup>$</sup><b>89</b><small>/month</small></div>
  <p class="desc">For growing businesses needing full compliance and multi-site control.</p>
  <ul><li>Up to 150 staff members</li><li>Up to 5 locations</li><li>Full compliance engine</li><li>Cost optimisation dashboard</li><li>Staff self-service portal</li><li>Payroll integrations</li><li>Priority support</li></ul>
  <span class="btn btn-primary" style="bottom:32px">Start Free Trial</span>
</div>
<div class="plan" style="left:800px">
  <div class="tier">ENTERPRISE</div>
  <div class="custom">Custom</div>
  <p class="desc" style="border:none;padding-bottom:0">Full-scale deployment for large organisations with complex, bespoke needs.</p>
  <ul style="margin-top:24px"><li>Unlimited staff &amp; locations</li><li>Custom compliance rules</li><li>Dedicated success manager</li><li>SSO &amp; advanced security</li><li>Custom API &amp; integrations</li><li>SLA guarantee &amp; 24/7 support</li><li>Onboarding &amp; training</li></ul>
  <span class="btn btn-ghost" style="bottom:32px">Talk to Sales</span>
</div>

<section class="cta abs">
  <div class="cta-inner">
    <div class="eyebrow center">GET STARTED TODAY</div>
    <h2>Ready to transform<br>your workforce?</h2>
    <p class="lead">Join 500+ companies saving time and money with Tidal Ledger. Setup takes under 15 minutes — your first roster is free.</p>
    <div class="cta-btns"><span class="btn btn-primary" style="background:var(--blue-700)">Start Free Trial →</span><span class="btn btn-ghost">Book a Demo</span></div>
  </div>
</section>

<section class="contact-head abs">
  <div class="eyebrow">GET IN TOUCH</div>
  <h2 class="h2">Let's talk about<br>your team</h2>
  <p class="lead">Book a personalised demo or ask us anything. Our team responds within one business day — no pressure, just a genuine conversation.</p>
  <div class="info">
    <div class="info-row"><i><svg width="14" height="12" viewBox="0 0 14 12"><rect x="1" y="1" width="12" height="10" rx="1.5" fill="none" stroke="#0677BA" stroke-width="1.4"/><path d="M1.5 2l5.5 4.5L12.5 2" fill="none" stroke="#0677BA" stroke-width="1.4"/></svg></i><div><b>Email</b><small>hello@tidalledger.example</small></div></div>
    <div class="info-row"><i><svg width="14" height="14" viewBox="0 0 14 14"><path d="M3 1.5l2 2.5-1.2 1.5c.8 1.8 2 3 3.7 3.7L9 8l2.5 2-1 2.3C5.5 12 2 8.5 1.7 2.5z" fill="#0E1A2B"/></svg></i><div><b>Phone</b><small>+1 (555) 010-4477</small></div></div>
    <div class="info-row"><i><svg width="12" height="14" viewBox="0 0 14 14"><path d="M8 1L3 8h4l-1 5 5-7H7z" fill="#0677BA"/></svg></i><div><b>Response Time</b><small>Within 1 business day</small></div></div>
  </div>
</section>
<form class="form abs">
  <div class="row2"><div class="field"><label>FIRST NAME</label><div class="input">Jane</div></div><div class="field"><label>LAST NAME</label><div class="input">Doe</div></div></div>
  <div class="field"><label>COMPANY</label><div class="input">Your Company</div></div>
  <div class="field"><label>WORK EMAIL</label><div class="input">jane@company.example</div></div>
  <div class="field"><label>TEAM SIZE</label><div class="input select">Select team size... <svg width="10" height="6" viewBox="0 0 10 6"><path d="M1 1l4 4 4-4" stroke="#33445A" stroke-width="1.5" fill="none"/></svg></div></div>
  <div class="field"><label>MESSAGE</label><div class="input textarea">Tell us about your scheduling challenges...</div></div>
  <span class="btn btn-primary">Send Message →</span>
</form>

<footer class="footer abs">
  <div class="brand"><span class="brand-dot" style="background:var(--blue-700)"></span>Tidal Ledger</div>
  <p class="about">AI-powered workforce scheduling for any industry. Save time, cut costs, stay compliant — all in one platform.</p>
  <div class="fcol" style="left:506px"><h4>PRODUCT</h4><a>Features</a><a>Pricing</a><a>Industries</a><a>Integrations</a><a>API Docs</a></div>
  <div class="fcol" style="left:728px"><h4>COMPANY</h4><a>About Us</a><a>Blog</a><a>Careers</a><a>Press</a><a>Contact</a></div>
  <div class="fcol" style="left:950px"><h4>LEGAL</h4><a>Privacy Policy</a><a>Terms of Service</a><a>Security</a><a>GDPR</a></div>
  <div class="fbottom"><span>© 2025 Tidal Ledger. All rights reserved.</span><span>Crafted with precision for operations leaders everywhere</span></div>
</footer>

</body>
</html>
```